Washing powder bag design.

Project Description – Graphic Design Proposal for ORNE Laundry Powder Packaging
We have already explored initial design ideas internally, supported by AI-assisted tools (ChatGPT) to develop early concepts, layouts, and mockups. To support this, we have attached the bag die-cut, where graphics and text are placed as a visual guideline for the intended structure. In addition, we have included a mockup of the product series currently under development to clearly communicate the desired style, direction, and overall visual identity.
The mockup should be regarded as the design foundation for this project and as a starting point for professional refinement.
Scope of Work
We would like you to create three graphic design variants, each based on a different color direction:
1. Variant 1: In line with our current color scheme
2. Variant 2: A blue version
3. Variant 3: A green version
Design Elements to Be Preserved
The following elements must be maintained across all three variants:
• The overall style and visual expression of the mockup
• The leaf-shaped element in the bottom right corner
• The ORNE layout, including typography, positioning, and general look & feel
Summary
While the color palette may vary, the structure, style, and key design elements must remain consistent and be directly based on the attached mockup.
We look forward to seeing your creative interpretation and professional input.
Updates
We need the design to be created based on the attached die-cut file “Orne 10 kg BAG 202526”, including all text elements.
We would like the final to include both the designed die-cut file and a mockup.

```html
<!DOCTYPE html>
<html lang="da">
<head>
<meta charset="utf-8">
<title>Orne Vaskepulver – Design Variants</title>
<link rel="stylesheet" href="https://fonts.googleapis.com/css2?family=Bebas+Neue&family=Roboto+Condensed:wght@300;400;500;700&family=Open+Sans:wght@300&display=swap">
<style>
  :root {
    --page-bg: #fdf0d8;
    --paper: #ffffff;
    --title-ink: #222222;
    --gold-ink: #b8862c;
    --gold-band: #eee2c4;
    --gold-tint: #f8ecd2;
    --green-ink: #2c6b36;
    --green-band: #d2e5d1;
    --green-tint: #e1efe2;
    --blue-ink: #204f8c;
    --blue-band: #d5e2f1;
    --blue-tint: #e5effa;
  }
  * { box-sizing: border-box; margin: 0; padding: 0; }
  html, body { width: 1200px; height: 1115px; overflow: hidden; }
  body { background: var(--page-bg); font-family: "Roboto Condensed", sans-serif; position: relative; }

  .sheet-title {
    position: absolute; top: 36px; left: 0; width: 1200px; text-align: center;
    font-family: "Open Sans", sans-serif; font-weight: 300; font-size: 36px;
    letter-spacing: -1px; color: var(--title-ink);
  }

  .variant-row { position: absolute; top: 130px; left: 50px; display: flex; gap: 40px; }

  .bag-front {
    position: relative; width: 340px; height: 940px; background: var(--paper);
    overflow: hidden; box-shadow: 0 6px 18px rgba(0,0,0,0.12);
  }
  .bag-front.gold  { --ink: var(--gold-ink);  --band: var(--gold-band);  --tint: var(--gold-tint); }
  .bag-front.green { --ink: var(--green-ink); --band: var(--green-band); --tint: var(--green-tint); }
  .bag-front.blue  { --ink: var(--blue-ink);  --band: var(--blue-band);  --tint: var(--blue-tint); }

  .lower-band { position: absolute; left: 0; right: 0; top: 560px; bottom: 0; background: var(--band); }

  .leaf-decor {
    position: absolute; left: 10px; top: 270px; width: 120px; height: 300px;
    border-radius: 60px; background: linear-gradient(180deg, var(--tint), rgba(255,255,255,0));
    opacity: 0.8;
  }
  .leaf-decor.right { left: auto; right: 8px; top: 200px; width: 70px; height: 200px; }

  .brand-badge {
    position: absolute; top: 150px; left: 80px; width: 180px; height: 180px;
    border-radius: 50%; background: var(--tint);
    display: flex; align-items: center; justify-content: center;
  }
  .brand-name { font-weight: 700; font-size: 56px; color: var(--ink); }

  .product-name {
    position: absolute; top: 418px; left: 0; width: 340px; text-align: center;
    font-family: "Bebas Neue", sans-serif; font-size: 66px; line-height: 1; color: var(--ink);
  }
  .subtitle {
    position: absolute; top: 500px; left: 45px; width: 250px; text-align: center;
    border-top: 2px solid var(--ink); border-bottom: 2px solid var(--ink);
    padding: 6px 0 4px; font-weight: 500; font-size: 20px; color: var(--ink);
  }
  .tagline {
    position: absolute; top: 582px; left: 0; width: 340px; text-align: center;
    font-weight: 400; font-size: 22px; line-height: 1.25; color: var(--ink);
  }

  .care-icons { position: absolute; top: 790px; left: 28px; display: flex; gap: 10px; }
  .care-icon {
    width: 36px; height: 36px; border-radius: 8px; background: var(--ink);
    display: flex; align-items: center; justify-content: center;
  }
  .care-icon span { color: #fff; font-weight: 700; font-size: 13px; border: 1.5px solid #fff; border-radius: 4px; padding: 2px 3px; }
  .care-icon svg { width: 26px; height: 26px; }
  .temperatures {
    position: absolute; top: 838px; left: 28px; font-weight: 700; font-size: 13px; color: var(--ink);
  }
  .net-weight { position: absolute; top: 780px; right: 26px; text-align: center; color: var(--ink); }
  .net-weight small { display: block; font-size: 11px; }
  .net-weight strong { font-family: "Bebas Neue", sans-serif; font-weight: 400; font-size: 40px; line-height: 1; }
</style>
</head>
<body>
  <h1 class="sheet-title">MOCKUP DESIGN</h1>

  <main class="variant-row">
    <section class="bag-front gold">
      <div class="lower-band"></div>
      <div class="leaf-decor" role="img" aria-label="Faint leaf branch decoration"></div>
      <div class="leaf-decor right" role="img" aria-label="Faint leaf branch decoration"></div>
      <div class="brand-badge"><span class="brand-name">Orne</span></div>
      <h2 class="product-name">VASKEPULVER</h2>
      <p class="subtitle">LAUNDRY DERERGENT</p>
      <p class="tagline">LIV OG BALANCE<br>I HVERDAGEN</p>
      <div class="care-icons">
        <div class="care-icon"><span>120</span></div>
        <div class="care-icon"><svg viewBox="0 0 26 26"><rect x="5" y="3" width="16" height="20" rx="2" fill="none" stroke="#fff" stroke-width="2"/><circle cx="13" cy="15" r="4.5" fill="none" stroke="#fff" stroke-width="2"/></svg></div>
        <div class="care-icon"><svg viewBox="0 0 26 26"><path d="M4 12 H22 L19 21 H7 Z" fill="none" stroke="#fff" stroke-width="2"/><path d="M10 11 L17 4" stroke="#fff" stroke-width="2.5" stroke-linecap="round"/></svg></div>
      </div>
      <p class="temperatures">20°C | 30°C | 40°C | 60°C | 90°C</p>
      <div class="net-weight"><small>Net Weight</small><strong>10KG</strong></div>
    </section>

    <section class="bag-front green">
      <div class="lower-band"></div>
      <div class="leaf-decor" role="img" aria-label="Faint leaf branch decoration"></div>
      <div class="leaf-decor right" role="img" aria-label="Faint leaf branch decoration"></div>
      <div class="brand-badge"><span class="brand-name">Orne</span></div>
      <h2 class="product-name">VASKEPULVER</h2>
      <p class="subtitle">LAUNDRY DERERGENT</p>
      <p class="tagline">LIV OG BALANCE<br>I HVERDAGEN</p>
      <div class="care-icons">
        <div class="care-icon"><span>120</span></div>
        <div class="care-icon"><svg viewBox="0 0 26 26"><rect x="5" y="3" width="16" height="20" rx="2" fill="none" stroke="#fff" stroke-width="2"/><circle cx="13" cy="15" r="4.5" fill="none" stroke="#fff" stroke-width="2"/></svg></div>
        <div class="care-icon"><svg viewBox="0 0 26 26"><path d="M4 12 H22 L19 21 H7 Z" fill="none" stroke="#fff" stroke-width="2"/><path d="M10 11 L17 4" stroke="#fff" stroke-width="2.5" stroke-linecap="round"/></svg></div>
      </div>
      <p class="temperatures">20°C | 30°C | 40°C | 60°C | 90°C</p>
      <div class="net-weight"><small>Net Weight</small><strong>10KG</strong></div>
    </section>

    <section class="bag-front blue">
      <div class="lower-band"></div>
      <div class="leaf-decor" role="img" aria-label="Faint leaf branch decoration"></div>
      <div class="leaf-decor right" role="img" aria-label="Faint leaf branch decoration"></div>
      <div class="brand-badge"><span class="brand-name">Orne</span></div>
      <h2 class="product-name">VASKEPULVER</h2>
      <p class="subtitle">LAUNDRY DERERGENT</p>
      <p class="tagline">LIV OG BALANCE<br>I HVERDAGEN</p>
      <div class="care-icons">
        <div class="care-icon"><span>120</span></div>
        <div class="care-icon"><svg viewBox="0 0 26 26"><rect x="5" y="3" width="16" height="20" rx="2" fill="none" stroke="#fff" stroke-width="2"/><circle cx="13" cy="15" r="4.5" fill="none" stroke="#fff" stroke-width="2"/></svg></div>
        <div class="care-icon"><svg viewBox="0 0 26 26"><path d="M4 12 H22 L19 21 H7 Z" fill="none" stroke="#fff" stroke-width="2"/><path d="M10 11 L17 4" stroke="#fff" stroke-width="2.5" stroke-linecap="round"/></svg></div>
      </div>
      <p class="temperatures">20°C | 30°C | 40°C | 60°C | 90°C</p>
      <div class="net-weight"><small>Net Weight</small><strong>10KG</strong></div>
    </section>
  </main>
</body>
</html>
```